Wedding and event Photography company.

We need a business card design for a photography company based in Singapore named TamKeza. Our core service offering is wedding photojournalism. We would like to see minimalistic designs that use the colour white. The final design should communicate a sense of ease and reliability.

The attached are a couple of visual reference which i found over the web, i hope it will helps.

Project Brief Update (14th July 2014):
- Please refrain from using any images from the website for the design. The laws and regulations over here does not allow me to distribute my client's images. Thanks!

Target Market(s)

Young and middle aged adults aged 24 - 38. With money to spend =D

Industry/Entity Type

Business

Contact Information for Business Card

Name: Dev Lunor
Designation: Head Photographer
Mobile: +65 81749026
Email: jun@tamkeza.example
Website: www.tamkeza.example

Font styles to use
Other font styles liked:
• Baskerville URW

Colors

Designer to choose colors to be used in the design.

Requirements
Must have
• Must include:
• - The brand TamKeza
• - The logo attached
• - Please help to place the brand TamKeza with the logo according to your preferences.
• - Services
• - Wedding Photography
• - Portraiture
• - Photojournalism
Nice to have
• Looking forward to an elegant and simple design. Please see attached examples!
• Please use Serif Fonts
Should not have
• Please refrain from using dark tones for the majority of the design.
• Please refrain from letterpress and embossing.

```html
<!DOCTYPE html>
<html lang="en">
<head>
<meta charset="utf-8">
<title>TamKeza Business Card</title>
<link rel="stylesheet" href="https://fonts.googleapis.com/css2?family=EB+Garamond:wght@400;500;700&display=swap">
<style>
  :root {
    --backdrop: #000000;
    --card: #f9f8f4;
    --panel: #eff0ed;
    --ink: #2a2a2a;
    --ink-soft: #4a4a4a;
    --rule: #6a6a6a;
  }
  * { margin: 0; padding: 0; box-sizing: border-box; }
  html, body {
    width: 1200px; height: 1000px; overflow: hidden;
    background: var(--backdrop);
    font-family: "EB Garamond", Georgia, serif;
    color: var(--ink);
  }
  .stage {
    position: relative; width: 1200px; height: 1000px;
    display: flex; align-items: center; justify-content: center; gap: 40px;
  }
  .card {
    position: relative; width: 520px; height: 312px;
    background: var(--card); border-radius: 22px; overflow: hidden;
  }

  /* Contact side */
  .card--contact .side-panel {
    position: absolute; left: 0; top: 0; width: 190px; height: 150px;
    background: var(--panel);
  }
  .identity {
    position: absolute; right: 36px; top: 42px; text-align: right;
  }
  .identity__name {
    font-size: 26px; font-weight: 700; letter-spacing: 0.02em; text-transform: uppercase;
  }
  .identity__role {
    font-size: 13px; font-weight: 500; letter-spacing: 0.03em; text-transform: uppercase;
    color: var(--ink-soft); margin-top: 2px;
  }
  .contacts {
    position: absolute; left: 36px; top: 120px; list-style: none;
    font-size: 13px; line-height: 1.5; letter-spacing: 0.02em; text-transform: uppercase;
    color: var(--ink-soft);
  }
  .registration {
    position: absolute; right: 36px; bottom: 34px;
    font-size: 12px; letter-spacing: 0.03em; text-transform: uppercase; color: var(--ink-soft);
  }

  /* Brand side */
  .card--brand .brand-field {
    position: absolute; left: 0; top: 0; width: 100%; height: 232px;
    background: var(--panel);
  }
  .brand {
    position: absolute; left: 0; right: 0; top: 96px;
    display: flex; flex-direction: column; align-items: center; gap: 14px;
  }
  .brand__mark {
    width: 14px; height: 14px; background: var(--ink);
  }
  .brand__name {
    font-size: 24px; font-weight: 500; letter-spacing: 0.28em; color: var(--ink);
  }
  .services {
    position: absolute; left: 0; right: 0; bottom: 28px;
    display: flex; justify-content: center; align-items: center; gap: 16px;
    font-size: 13.5px; letter-spacing: 0.05em; text-transform: uppercase; color: var(--ink-soft);
  }
  .services__divider { width: 1px; height: 14px; background: var(--rule); }
</style>
</head>
<body>
  <main class="stage">
    <section class="card card--contact" aria-label="Business card, contact side">
      <div class="side-panel"></div>
      <div class="identity">
        <h1 class="identity__name">Dev Lunor</h1>
        <p class="identity__role">Head Photographer</p>
      </div>
      <ul class="contacts">
        <li>+65 81749026</li>
        <li>jun@tamkeza.example</li>
        <li>www.tamkeza.example</li>
      </ul>
      <p class="registration">Business Reg No 48120957K</p>
    </section>

    <section class="card card--brand" aria-label="Business card, brand side">
      <div class="brand-field"></div>
      <div class="brand">
        <span class="brand__mark"></span>
        <span class="brand__name">TamKeza</span>
      </div>
      <p class="services">
        <span>Wedding Photography</span>
        <span class="services__divider"></span>
        <span>Portraiture</span>
        <span class="services__divider"></span>
        <span>Photo Journalism</span>
      </p>
    </section>
  </main>
</body>
</html>
```